Bramwell Quayle Lending Solutions business card design

Need a business card design for my mortgage broking business Bramwell Quayle Lending Solutions.

Target Market(s)

Mortgage clients/colleagues

Industry/Entity Type

Business

Requirements
Must have
• Must utilise logo attached. Possibly have logo only on back of card. my name & contact details on front and something creative?

Must incorporate purple/black/white in colour scheme.

Must incorporate tag line 'your loan navigators' under logo - using a script style fint. UPDATE: Mistral doesn't seem to be working on the card. Happy for you to try a different font. preferably a script style font.

Standard business card size.
Nice to have
• Try and incorporate the detective theme - but keep it looking sharp and professional.
Have attached some sample designs - does not have to be this - happy to review any ideas you may have.

```html
<!DOCTYPE html>
<html lang="en">
<head>
<meta charset="utf-8">
<title>Bramwell Quayle Lending Solutions – Business Card</title>
<link rel="stylesheet" href="https://fonts.googleapis.com/css2?family=Dancing+Script:wght@600&family=Open+Sans:wght@400&family=Oswald:wght@500&family=Raleway:wght@300&display=swap">
<style>
  :root {
    --purple: #4a2a8c;
    --purple-deep: #321a6a;
    --purple-light: #5b36a8;
    --white: #ffffff;
    --paper: #f3f3f3;
    --ink: #3a3a3a;
    --rule: #9a9a9a;
    --backdrop: #e6e4e0;
  }
  * { margin: 0; padding: 0; box-sizing: border-box; }
  html, body { width: 1200px; height: 1024px; overflow: hidden; }
  body {
    background: var(--backdrop);
    position: relative;
    font-family: "Open Sans", Arial, sans-serif;
  }
  .card {
    position: absolute;
    left: 250px;
    width: 700px;
    height: 400px;
    overflow: hidden;
    box-shadow: 0 6px 18px rgba(0,0,0,0.18);
  }

  /* Back of card */
  .card-back {
    top: 80px;
    background: radial-gradient(ellipse at 45% 40%, var(--purple-light) 0%, var(--purple) 45%, var(--purple-deep) 100%);
    color: var(--white);
  }
  .card-back .brand {
    position: absolute;
    left: 90px;
    top: 110px;
    display: flex;
    align-items: center;
    gap: 18px;
    font-family: "Raleway", Arial, sans-serif;
    font-weight: 300;
    color: var(--white);
  }
  .card-back .brand-dot {
    width: 22px; height: 22px; border-radius: 50%;
    background: var(--white);
    flex: none;
  }
  .card-back .brand-name { font-size: 58px; line-height: 1; letter-spacing: 1px; }
  .card-back .brand-sub { font-size: 22px; letter-spacing: 6px; margin-top: 10px; }
  .card-back .tagline-row {
    position: absolute;
    left: 130px;
    right: 0;
    top: 258px;
    display: flex;
    align-items: center;
    gap: 18px;
  }
  .card-back .tagline {
    font-family: "Dancing Script", cursive;
    font-weight: 600;
    font-size: 42px;
    white-space: nowrap;
  }
  .card-back .tagline-rule {
    flex: 1;
    height: 1px;
    background: rgba(255,255,255,0.8);
  }

  /* Front of card */
  .card-front {
    top: 544px;
    background: linear-gradient(160deg, var(--white) 0%, var(--paper) 100%);
    color: var(--ink);
  }
  .card-front .edge-band {
    position: absolute;
    left: 0; top: 0;
    width: 100%; height: 34px;
    background: var(--purple);
  }
  .card-front .contact-list {
    position: absolute;
    left: 48px;
    top: 74px;
    list-style: none;
    display: flex;
    flex-direction: column;
    gap: 16px;
    font-size: 19px;
  }
  .card-front .contact-list li { display: flex; align-items: center; gap: 16px; }
  .card-front .icon { width: 22px; height: 22px; flex: none; }
  .card-front .divider {
    position: absolute;
    left: 40px; right: 40px;
    top: 214px;
    height: 1px;
    background: var(--rule);
  }
  .card-front .brand {
    position: absolute;
    left: 48px;
    top: 246px;
    font-family: "Raleway", Arial, sans-serif;
    font-weight: 300;
    color: var(--purple);
    line-height: 1.1;
  }
  .card-front .brand-name { font-size: 38px; }
  .card-front .brand-sub { font-size: 16px; letter-spacing: 4px; margin-top: 6px; }
  .card-front .person {
    position: absolute;
    right: 48px;
    top: 250px;
    text-align: right;
  }
  .card-front .person-name {
    font-family: "Oswald", Arial, sans-serif;
    font-weight: 500;
    font-size: 38px;
    color: var(--purple);
    line-height: 1.1;
  }
  .card-front .person-title {
    font-family: "Oswald", Arial, sans-serif;
    font-weight: 500;
    font-size: 18px;
    color: var(--ink);
    margin-top: 6px;
  }
  .card-front .person-rule {
    width: 300px; height: 1px; background: var(--rule);
    margin: 16px 0 0 auto;
  }
</style>
</head>
<body>

<section class="card card-back">
  <div class="brand">
    <span class="brand-dot"></span>
    <div>
      <div class="brand-name">Bramwell Quayle</div>
      <div class="brand-sub">LENDING SOLUTIONS</div>
    </div>
  </div>
  <div class="tagline-row">
    <span class="tagline">your loan navigators</span>
    <span class="tagline-rule"></span>
  </div>
</section>

<section class="card card-front">
  <div class="edge-band"></div>
  <ul class="contact-list">
    <li>
      <svg class="icon" viewBox="0 0 22 22" aria-hidden="true">
        <circle cx="11" cy="11" r="11" fill="#4a2a8c"/>
        <path d="M7.5 5.5 L9.5 5.5 L10.3 8.3 L9 9.4 Q10 11.8 12.6 13 L13.7 11.7 L16.5 12.5 L16.5 14.5 Q15.8 16.2 13.8 16 Q7 14.6 6 8.2 Q5.9 6.2 7.5 5.5 Z" fill="#fff"/>
      </svg>
      <span>210-555-0147</span>
    </li>
    <li>
      <svg class="icon" viewBox="0 0 22 22" aria-hidden="true">
        <circle cx="11" cy="11" r="11" fill="#4a2a8c"/>
        <rect x="5.5" y="7" width="11" height="8" fill="none" stroke="#fff" stroke-width="1.4"/>
        <path d="M5.5 7 L11 11.5 L16.5 7" fill="none" stroke="#fff" stroke-width="1.4"/>
      </svg>
      <span>rosalind@bquayle.com</span>
    </li>
    <li>
      <svg class="icon" viewBox="0 0 22 22" aria-hidden="true">
        <circle cx="11" cy="11" r="11" fill="#4a2a8c"/>
        <circle cx="11" cy="11" r="5.8" fill="none" stroke="#fff" stroke-width="1.3"/>
        <ellipse cx="11" cy="11" rx="2.6" ry="5.8" fill="none" stroke="#fff" stroke-width="1.1"/>
        <path d="M5.2 11 H16.8" stroke="#fff" stroke-width="1.1"/>
      </svg>
      <span>www.bquayle.com</span>
    </li>
  </ul>
  <div class="divider"></div>
  <div class="brand">
    <div class="brand-name">Bramwell Quayle</div>
    <div class="brand-sub">LENDING SOLUTIONS</div>
  </div>
  <div class="person">
    <div class="person-name">Rosalind Marsh</div>
    <div class="person-title">Managing Director</div>
    <div class="person-rule"></div>
  </div>
</section>

</body>
</html>
```